Solar Energy Company Flyer/Door Hanger

Hello designers,

We are a solar energy company looking to make an eye-catching design for residential door hangers. These will be the type of door hangers that just stick to the door, not actually hang on the door. So essentially it will be a flyer that is 5.5" x 8.5" front and back. Please see attached template design for specifications and standards for print. The file will need to be provided in an editable PSD format.

Content for Flyer:

Front: Should be something eye caching, attention grabber, with big words and a visual of something to do with a nice looking home that has solar panels on it. Call to action should be at the bottom.

Words should ready: MAKE CENTS OUT OF SOLAR

Call to action link: apply.brivenpower.net

Back: Should have more in depth content. Company logo on back, 4 bullet points (checkmarks) with text, a chart (attached), and contact info at bottom. We will update content for the back soon, but please put together a layout that doesn't look plain jane and has some creativeness to it.

Update on content will be soon. If you want you can submit the front first and the back after.

Thanks!

Target Market(s)

Residential Home Owners

Industry/Entity Type

Solar Energy

Requirements
Must have
• Front should be clean and eycatching, back should be creative yet informational

```html
<!DOCTYPE html>
<html lang="en">
<head>
<meta charset="utf-8">
<title>Briven Solar – Door Flyer, Back and Front</title>
<link rel="stylesheet" href="https://fonts.googleapis.com/css2?family=Roboto+Condensed:wght@400;700&family=Questrial&display=swap">
<style>
  :root{
    --orange:#ee7429;
    --ink:#1d1d1d;
    --paper:#ffffff;
    --backdrop:#3a2418;
    --green:#2e8b3e;
    --green-light:#9cc57a;
    --slate:#6f8591;
  }
  *{box-sizing:border-box;margin:0;padding:0}
  html,body{width:1200px;height:1200px;overflow:hidden;background:var(--backdrop)}
  .stage{position:relative;width:1200px;height:1200px}
  .flyer{position:absolute;width:470px;height:718px;background:var(--paper);overflow:hidden;
    font-family:"Roboto Condensed",sans-serif;color:var(--ink)}
  .flyer--back{left:132px;top:140px}
  .flyer--front{left:642px;top:323px}

  .header-art{position:absolute;left:0;top:0;width:470px}
  .brand{position:absolute;left:34px;top:62px;font-family:"Roboto Condensed",sans-serif;
    font-weight:700;font-size:30px;line-height:34px;color:var(--ink);letter-spacing:-.3px;white-space:nowrap}

  .intro{position:absolute;left:22px;top:262px;width:428px;height:54px;background:var(--orange);
    border-radius:9px;color:#fff;font-size:10.6px;line-height:14px;padding:5px 11px;text-align:justify}

  .checklist{position:absolute;left:32px;top:326px;width:410px;list-style:none}
  .checklist li{display:flex;gap:12px;font-size:10.6px;line-height:13.5px;height:33.5px}
  .checklist svg{flex:none;width:16px;height:16px;margin-top:-1px}

  .savings-chart{position:absolute;left:32px;top:456px;width:200px;height:88px}
  .gallery{position:absolute;display:block}
  .g1{left:238px;top:458px;width:201px;height:84px}
  .g2{left:32px;top:546px;width:200px;height:85px}
  .g3{left:238px;top:546px;width:201px;height:85px}

  .footer{position:absolute;left:0;bottom:0;width:470px;height:80px;background:var(--orange);
    color:#fff;text-align:center;padding-top:12px}
  .footer__name{font-weight:700;font-size:17px;line-height:22px}
  .footer__contact{font-size:12px;line-height:18px;margin-top:2px;white-space:nowrap}
  .footer__contact span{margin:0 6px}

  .headline{position:absolute;right:31px;top:140px;width:300px;height:170px;color:#fff;
    font-family:"Questrial",sans-serif;font-weight:400}
  .headline__line{position:absolute;right:0;display:block;white-space:nowrap;line-height:1}
  .headline__line--one{top:0;font-size:42px}
  .headline__line--two{top:52px;font-size:42px}
  .headline__line--big{top:104px;font-size:66px;letter-spacing:1px}
</style>
</head>
<body>
<main class="stage">

  <section class="flyer flyer--back">
    <svg class="header-art" viewBox="0 0 470 254" width="470" height="254" role="img" aria-label="Photo of a ground-mounted solar array in the desert">
      <defs>
        <linearGradient id="desertTone" x1="0" y1="0" x2="0" y2="1">
          <stop offset="0" stop-color="#d9dfe0"/>
          <stop offset=".35" stop-color="#9aa57e"/>
          <stop offset=".55" stop-color="#3b5aa6"/>
          <stop offset=".8" stop-color="#2f4f9c"/>
          <stop offset="1" stop-color="#e6cdb4"/>
        </linearGradient>
      </defs>
      <polygon points="0,208 366,46 470,94 470,254 0,254" fill="url(#desertTone)"/>
      <polyline points="0,208 366,46 470,94" fill="none" stroke="var(--orange)" stroke-width="3"/>
    </svg>
    <div class="brand">Briven Solar</div>

    <p class="intro">Briven Power Solutions is dedicated to providing clean sustainable energy for the commercial and utility clients throughout North America. Since being established in 2011, we have focused on meeting every changing need of our customers.</p>

    <ul class="checklist">
      <li><svg viewBox="0 0 16 16"><rect x="1" y="3" width="12" height="12" fill="none" stroke="#1d1d1d" stroke-width="1.6"/><path d="M3.5 8.5l3 3L15 1.5" fill="none" stroke="#1d1d1d" stroke-width="2"/></svg><span>Many desktop publishing packages and web page editors now use Lorem Ipsum as their default model text,</span></li>
      <li><svg viewBox="0 0 16 16"><rect x="1" y="3" width="12" height="12" fill="none" stroke="#1d1d1d" stroke-width="1.6"/><path d="M3.5 8.5l3 3L15 1.5" fill="none" stroke="#1d1d1d" stroke-width="2"/></svg><span>Many desktop publishing packages and web page editors now use Lorem Ipsum as their default model text,</span></li>
      <li><svg viewBox="0 0 16 16"><rect x="1" y="3" width="12" height="12" fill="none" stroke="#1d1d1d" stroke-width="1.6"/><path d="M3.5 8.5l3 3L15 1.5" fill="none" stroke="#1d1d1d" stroke-width="2"/></svg><span>Many desktop publishing packages and web page editors now use Lorem Ipsum as their default model text,</span></li>
      <li><svg viewBox="0 0 16 16"><rect x="1" y="3" width="12" height="12" fill="none" stroke="#1d1d1d" stroke-width="1.6"/><path d="M3.5 8.5l3 3L15 1.5" fill="none" stroke="#1d1d1d" stroke-width="2"/></svg><span>Many desktop publishing packages and web page editors now use Lorem Ipsum as their default model text,</span></li>
    </ul>

    <svg class="savings-chart" viewBox="0 0 200 88" role="img" aria-label="Chart: utility bill without solar rises over 20 years while solar payment stays flat, showing savings">
      <polygon points="2,50 183,2 183,70 2,70" fill="var(--slate)"/>
      <polygon points="2,58 183,36 183,70 2,70" fill="var(--green-light)"/>
      <polygon points="2,66 183,60 183,70 2,70" fill="var(--green)"/>
      <text x="20" y="48" transform="rotate(-13 20 48)" font-family="Roboto Condensed,sans-serif" font-size="6.5" font-weight="700" fill="#fff" letter-spacing=".6">UTILITY BILL WITHOUT SOLAR</text>
      <text x="22" y="62" transform="rotate(-5 22 62)" font-family="Roboto Condensed,sans-serif" font-size="5.5" font-weight="700" fill="#fff" letter-spacing=".5">SOLAR PAYMENT</text>
      <text x="22" y="69" transform="rotate(-2 22 69)" font-family="Roboto Condensed,sans-serif" font-size="5.5" font-weight="700" fill="#fff" letter-spacing=".5">UTILITY BILL WITH SOLAR</text>
      <text x="197" y="40" transform="rotate(-90 197 40)" font-family="Roboto Condensed,sans-serif" font-size="9" font-weight="700" fill="var(--green)">SAVINGS</text>
      <text x="4" y="82" font-family="Roboto Condensed,sans-serif" font-size="6" font-weight="700" fill="#888">Year 1</text>
      <text x="84" y="82" font-family="Roboto Condensed,sans-serif" font-size="6" font-weight="700" fill="#888">Year 10</text>
      <text x="164" y="82" font-family="Roboto Condensed,sans-serif" font-size="6" font-weight="700" fill="#888">Year 20</text>
    </svg>

    <svg class="gallery g1" viewBox="0 0 10 10" preserveAspectRatio="none" role="img" aria-label="Photo of solar panels on a tiled roof">
      <defs><linearGradient id="g1Tone" x1="0" y1="0" x2="1" y2="1"><stop offset="0" stop-color="#8a8f98"/><stop offset=".5" stop-color="#2d4f9e"/><stop offset="1" stop-color="#b8573a"/></linearGradient></defs>
      <rect width="10" height="10" fill="url(#g1Tone)"/>
    </svg>
    <svg class="gallery g2" viewBox="0 0 10 10" preserveAspectRatio="none" role="img" aria-label="Photo of installers fitting solar panels on a flat roof">
      <defs><linearGradient id="g2Tone" x1="0" y1="0" x2="0" y2="1"><stop offset="0" stop-color="#587a4e"/><stop offset=".4" stop-color="#4568a8"/><stop offset="1" stop-color="#344f8e"/></linearGradient></defs>
      <rect width="10" height="10" fill="url(#g2Tone)"/>
    </svg>
    <svg class="gallery g3" viewBox="0 0 10 10" preserveAspectRatio="none" role="img" aria-label="Photo of a rooftop solar array with houses behind">
      <defs><linearGradient id="g3Tone" x1="0" y1="0" x2="0" y2="1"><stop offset="0" stop-color="#c9cfd6"/><stop offset=".35" stop-color="#b99a7c"/><stop offset=".55" stop-color="#4a6aa8"/><stop offset="1" stop-color="#3c5b9c"/></linearGradient></defs>
      <rect width="10" height="10" fill="url(#g3Tone)"/>
    </svg>

    <footer class="footer">
      <div class="footer__name">Briven Power Solutions, LLC.</div>
      <div class="footer__contact">Meridian Plaza, Downtown Lakeview<span>|</span>(555) 014-2290<span>|</span>info@brivenpower.net</div>
    </footer>
  </section>

  <section class="flyer flyer--front">
    <svg class="header-art" viewBox="0 0 470 638" width="470" height="638" role="img" aria-label="Photo of a white house with an orange tiled roof covered in solar panels under a blue sky">
      <defs>
        <linearGradient id="houseTone" x1="0" y1="0" x2="0" y2="1">
          <stop offset="0" stop-color="#8fb0e2"/>
          <stop offset=".5" stop-color="#c3d5ee"/>
          <stop offset=".66" stop-color="#c8714a"/>
          <stop offset=".78" stop-color="#3f62b0"/>
          <stop offset=".9" stop-color="#e9e6df"/>
          <stop offset="1" stop-color="#5f8a3c"/>
        </linearGradient>
      </defs>
      <polygon points="0,208 366,46 470,94 470,638 0,638" fill="url(#houseTone)"/>
      <polyline points="0,208 366,46 470,94" fill="none" stroke="var(--orange)" stroke-width="3"/>
    </svg>
    <div class="brand">Briven Solar</div>

    <h1 class="headline">
      <span class="headline__line headline__line--one">MAKE CENTS</span>
      <span class="headline__line headline__line--two">OUT OF</span>
      <span class="headline__line headline__line--big">SOLAR</span>
    </h1>

    <footer class="footer">
      <div class="footer__name">Briven Power Solutions, LLC.</div>
      <div class="footer__contact">Meridian Plaza, Downtown Lakeview<span>|</span>(555) 014-2290<span>|</span>info@brivenpower.net</div>
    </footer>
  </section>

</main>
</body>
</html>
```